Local Chiropractor Needs Up Scale Webdesign

This website needs to have an upscale look with a very modern feel. Below is the information and websites to reference

Add Logo that is attached

Build a color scheme similar to this website image titled "chiro-1"

Must Include these pages in a horizontal menu bar in this order:
Home, Meet Our Staff, Patient Testimonials, Videos, Work Place Wellness, Contact

Build a "classy looking" Make An Appointment Button into the header with the contact info below

Phone Number:
555-314-2706

Address:
4318 Willow Barn Lane, #215
Maple Hollow, WS 55492

This website needs 4 rotating banners. Please reference a layout similar to this for the banners: http://drkelmora.com/. However design it nicer than this website, this website is very boring and doesn't flow with the colors properly

Below are the description for each banner

Rotating Banner #1
Use Image: Pediatrics
Two lines of text. First line title line, second description. Use Latin text for fill

Rotating Banner #2
Use Image: Aging Gracefully

Rotating Banner #3
Use Image: Pregnancy

Rotating Banner #4
Use Image: Athletics

I'd like to see a free consultation box similar to the "chiro-1" image. Fields to include are: First Name, Last Name, Phone Number, Comments.

For the body, please fill it with latin text. Please design a professional body layout. You can include a box in the right column for the hours

Office Hours
Monday: 8:00-11:00, 2:00-5:00
Tuesday: 8:30-11:00, 2:00-5:30
Wednesday: 8:00-11:00, 2:00-5:00
Thursday: 10:00-12:00, 2:30-5:00
Friday: 8:00-10:00, 1:00-5:00
Saturday: Closed
Sunday: Closed

For the footer please design something similar to the: http://drkelmora.com/

Also include in the Footer: Powered by Tandem Pixel Works

```html
<!DOCTYPE html>
<html lang="en">
<head>
<meta charset="utf-8">
<title>Local Chiropractor</title>
<link href="https://fonts.googleapis.com/css2?family=Raleway:wght@400;500&family=Open+Sans:ital,wght@0,400;0,600;1,400&display=swap" rel="stylesheet">
<style>
:root{
  --green:#8cc63f;
  --green-dark:#6a9a3a;
  --green-text:#93c83e;
  --black:#141414;
  --charcoal:#2b2b2b;
  --grey-text:#666;
  --white:#fff;
}
*{box-sizing:border-box;margin:0;padding:0}
html,body{width:926px;height:1200px;overflow:hidden;background:var(--white)}
body{position:relative;font-family:"Open Sans",Arial,sans-serif;color:#333}
.abs{position:absolute}
.site-header{left:0;top:0;width:926px;height:78px;background:var(--black)}
.brand{left:107px;top:24px;font-family:"Raleway",sans-serif;font-weight:400;font-size:28px;color:var(--white);letter-spacing:.2px}
.btn-appointment{left:559px;top:41px;width:114px;height:24px;background:var(--green);color:var(--white);font-size:11px;text-align:center;line-height:24px}
.header-contact{left:687px;top:18px;color:var(--white);font-size:10.5px;line-height:14.5px;white-space:nowrap}
.header-contact .phone{color:var(--green-text);font-size:14px;margin-top:3px}
.main-nav{left:0;top:78px;width:926px;height:29px;background:linear-gradient(#9ccf4c,#86bf36)}
.main-nav ul{list-style:none;display:flex;padding-left:130px}
.main-nav li{color:var(--white);font-size:11.5px;line-height:29px;margin-right:24.5px}
.hero{left:0;top:107px;width:926px;height:395px;background:linear-gradient(100deg,#f3f4ee 0%,#eef0e6 30%,#d9dcc8 48%,#c9b49a 62%,#e7d8c6 72%,#b9c471 88%,#a8c04e 100%)}
.hero-text{left:105px;top:228px}
.hero-title{font-family:"Raleway",sans-serif;font-size:30px;color:var(--green-text);font-weight:500}
.hero-sub{font-family:"Raleway",sans-serif;font-size:19px;color:#222;margin-top:2px}
.hero-copy{font-size:7.5px;color:#444;line-height:13.5px;margin-top:7px;width:260px}
.dots{left:105px;top:329px;display:flex;gap:3px}
.dots i{width:11px;height:11px;border-radius:50%;border:1px solid var(--green);background:var(--white)}
.dots i.on{background:var(--green)}
.hero-next{left:836px;top:280px}
.feature{top:467px;width:237px;height:149px;color:var(--white);padding:24px 0 0 26px}
.feature h3{font-family:"Raleway",sans-serif;font-weight:400;font-size:17px}
.feature p{font-size:8px;line-height:13.5px;margin-top:5px;width:130px}
.feature .btn{display:inline-block;border:1.5px solid var(--white);font-size:7.5px;padding:5px 12px;margin-top:10px}
.feature svg{position:absolute;right:30px;top:40px}
.f1{left:107px;background:var(--green-dark)}
.f2{left:344px;background:var(--green)}
.f3{left:581px;width:238px;background:var(--charcoal);padding-left:21px;padding-top:22px}
.f3 h3{font-size:17.5px}
.welcome{left:100px;top:650px;width:465px}
.welcome h1{font-family:"Raleway",sans-serif;font-weight:400;font-size:21px;color:#333}
.welcome p{font-size:7.6px;color:var(--grey-text);line-height:13.5px;margin-top:6px;padding-left:4px}
.stories-title{left:105px;top:779px;font-family:"Raleway",sans-serif;font-weight:400;font-size:15px;color:#222}
.story{top:811px;width:230px}
.story .avatar{position:absolute;left:0;top:0;width:61px;height:61px;border-radius:50%}
.story blockquote{position:absolute;left:66px;top:0;width:152px;font-style:italic;font-size:7.5px;color:#888;line-height:13.5px}
.story cite{position:absolute;left:66px;top:70px;font-style:normal;font-size:7.5px;color:#333;white-space:nowrap}
.s1{left:104px}.s1 .avatar{background:radial-gradient(circle at 50% 40%,#d8a88f,#3b3b3b 70%)}
.s2{left:333px}.s2 .avatar{background:radial-gradient(circle at 50% 45%,#d9a07d,#5a3420 70%)}
.consult{left:606px;top:659px;width:213px;height:244px;border:1px solid #ddd;border-radius:2px;background:var(--white)}
.consult-head{left:0;top:0;width:213px}
.consult-head .txt{position:absolute;left:0;top:10px;width:213px;text-align:center;color:var(--white)}
.consult-head small{font-size:7.5px;letter-spacing:.6px;color:#bbb;display:block}
.consult-head strong{font-family:"Raleway",sans-serif;font-weight:500;font-size:14px;display:block;margin-top:1px}
.consult-head em{font-style:normal;color:var(--green-text);font-size:11px;display:block}
.field{left:20px;width:177px;height:20px;border:1px solid #ddd;background:linear-gradient(#fff,#f2f2f2);font-size:7.5px;color:#888;padding:5px 8px}
.field.tall{height:46px}
.btn-book{left:20px;top:204px;width:91px;height:24px;background:var(--green);color:var(--white);font-size:10.5px;line-height:24px;text-align:center}
.site-footer{left:0;top:960px;width:926px;height:240px;background:linear-gradient(#484848,#1c1c1c 40%,#161616)}
.site-footer h4{position:absolute;font-weight:400;font-size:11px;color:var(--white);letter-spacing:.2px}
.f-label{font-size:8px;color:var(--green-text);font-weight:600}
.f-text{font-size:8px;color:var(--white);line-height:15.5px;white-space:nowrap}
.map{left:246px;top:1014px;width:149px;height:84px;background:linear-gradient(135deg,#e6e4da,#d8d6cc 50%,#ece9dc)}
.hours{left:478px;top:1010px;font-size:8px;color:var(--white)}
.hours table{border-collapse:collapse}
.hours td{height:16px;padding:0;white-space:nowrap}
.social{left:478px;top:1085px;display:flex;gap:7px}
.social i{width:14px;height:14px;border-radius:2px;background:#ddd}
.f-rule{left:107px;top:1128px;width:708px;height:1px;background:#444}
.f-nav{left:109px;top:1144px;font-size:9.5px;color:#ddd;word-spacing:1px}
.copy{left:109px;top:1164px;font-size:7.5px;color:#999}
.powered{left:705px;top:1147px;font-size:7.5px;color:#aaa}
</style>
</head>
<body>

<header class="site-header abs">
  <div class="brand abs">Local Chiropractor</div>
  <div class="btn-appointment abs">Fix Appointment</div>
  <div class="header-contact abs">
    4318 Willow Barn Lane, #215<br>Maple Hollow, WS 55492
    <div class="phone">555-314-2706</div>
  </div>
</header>

<nav class="main-nav abs">
  <ul><li>Home</li><li>Meet Our Staff</li><li>Patient Testimonials</li><li>Videos</li><li>Work Place Wellness</li><li>Contact</li></ul>
</nav>

<section class="hero abs" role="img" aria-label="Smiling mother holding a toddler outdoors on a sunny green meadow"></section>
<div class="hero-text abs">
  <div class="hero-title">Mauris vel lacus vitae</div>
  <div class="hero-sub">Etiam est nunc venenatis</div>
  <p class="hero-copy">Etiam est nunc venenatis in tristique eu imperdiet ac nisl Cum sociis natoque penatibus et magnis dis parturient montes nasce</p>
</div>
<div class="dots abs"><i class="on"></i><i></i><i></i><i></i></div>
<svg class="hero-next abs" width="20" height="46" viewBox="0 0 20 46"><path d="M3 2 L17 23 L3 44" fill="none" stroke="#3f6f8a" stroke-width="1.5"/></svg>

<div class="feature f1 abs">
  <h3>What We Do</h3>
  <p>Mauris vel lacus vitae felis vestibulum volutpatc massa Etiam eu urna Sed porta Suspendisse quam leo molestie sed luctus</p>
  <span class="btn">READ MORE</span>
  <svg width="42" height="48" viewBox="0 0 42 48" fill="none" stroke="#fff" stroke-width="3.5" stroke-linecap="round"><path d="M4 4 V18 a10 10 0 0 0 20 0 V4"/><path d="M14 28 V36 a8 8 0 0 0 16 0 V26"/><circle cx="30" cy="21" r="5"/></svg>
</div>
<div class="feature f2 abs">
  <h3>Meet Our Staff</h3>
  <p>Mauris vel lacus vitae felis vestibulum volutpatc massa Etiam eu urna Sed porta Suspendisse quam leo molestie sed</p>
  <span class="btn">CLICK HERE</span>
  <svg width="42" height="48" viewBox="0 0 42 48" fill="#fff"><circle cx="21" cy="11" r="10"/><path d="M2 48 V36 a14 12 0 0 1 38 0 V48 Z"/><circle cx="13" cy="40" r="3" fill="#8cc63f"/><circle cx="29" cy="40" r="3" fill="#8cc63f"/></svg>
</div>
<div class="feature f3 abs">
  <h3>Services Provides</h3>
  <p>Mauris vel lacus vitae felis vestibulum volutpatc massa Etiam eu urna Sed porta Suspendisse quam leo molestie sed luctus</p>
  <span class="btn">READ MORE</span>
  <svg width="40" height="48" viewBox="0 0 40 48" fill="#fff"><path d="M4 46 Q14 30 20 22" stroke="#fff" stroke-width="2.5" fill="none"/><path d="M20 22 Q14 8 20 0 Q28 10 20 22Z"/><path d="M18 26 Q30 14 40 18 Q32 30 18 26Z"/><path d="M14 30 Q2 26 0 16 Q12 16 14 30Z"/><path d="M12 36 Q22 30 32 34 Q22 42 12 36Z"/></svg>
</div>

<section class="welcome abs">
  <h1>Welcome to Our Website Mainpage</h1>
  <p>Mauris vel lacus vitae felis vestibulum volutpat Etiam est nunc venenatis in tristique eu imperdiet ac nisl Cum sociis natoque penatibus et magnis dis parturient montes nascetur ridiculus mus In iaculis facilisis massa Etiam eu urna Sed porta Suspendisse quam leo molestie sed luctus quis feugiat in pede</p>
  <p>Curabitur iaculis tempus eros Curabitur vel mi sit amet magna malesuada ultrices Ut nisi erat fermentum vel congue id euismod in elit Fusce ultricies orci ac feugiat suscipit leo massa sodales velit et scelerisque mi tortor at ipsum</p>
</section>

<h2 class="stories-title abs">Success Stories</h2>
<div class="story s1 abs">
  <div class="avatar" role="img" aria-label="Portrait photo of a smiling older man"></div>
  <blockquote>Mauris vel lacus vitae felis vestibulum volutpat Etiam est nunc ven enatis in tris-tique eu imperdiet ac nisl Cum sociis natoque penatibus et magnis dis parturi-ent montes nascetur ridiculus mu</blockquote>
  <cite>By Author Name</cite>
</div>
<div class="story s2 abs">
  <div class="avatar" role="img" aria-label="Portrait photo of a smiling woman"></div>
  <blockquote>Mauris vel lacus vitae felis vestibulum volutpat Etiam est nunc ven enatis in tris-tique eu imperdiet ac nisl Cum sociis natoque penatibus et magnis dis parturi-ent montes nascetur ridiculus mu</blockquote>
  <cite>By Author Name</cite>
</div>

<aside class="consult abs">
  <div class="consult-head abs">
    <svg width="213" height="70" viewBox="0 0 213 70"><defs><linearGradient id="ch" x1="0" y1="0" x2="0" y2="1"><stop offset="0" stop-color="#3a3a3a"/><stop offset="1" stop-color="#121212"/></linearGradient></defs><path d="M0 0 H213 V52 L106 70 L0 52 Z" fill="url(#ch)"/><line x1="38" y1="46" x2="84" y2="46" stroke="#888" stroke-width=".7"/><line x1="129" y1="46" x2="175" y2="46" stroke="#888" stroke-width=".7"/></svg>
    <div class="txt"><small>CONTACT US NOW AND GET YOUR</small><strong>FREE CONSULTATION</strong><em>TODAY!</em></div>
  </div>
  <div class="field abs" style="top:76px">Your Name</div>
  <div class="field abs" style="top:101px">Email address</div>
  <div class="field abs" style="top:126px">Phone no.</div>
  <div class="field tall abs" style="top:151px">Comments</div>
  <div class="btn-book abs">BOOK NOW</div>
</aside>

<footer class="site-footer abs">
  <h4 style="left:119px;top:31px">CONTACT US</h4>
  <div class="abs" style="left:119px;top:53px">
    <div class="f-label">Address:</div>
    <div class="f-text">4318 Willow Barn Lane, #215<br>Maple Hollow, WS 55492</div>
    <div class="f-label" style="margin-top:6px">Phone Number:</div>
    <div class="f-text" style="font-size:11px;margin-top:2px">555-314-2706</div>
  </div>
  <h4 style="left:478px;top:31px">OFFICE HOURS</h4>
</footer>
<div class="map abs" role="img" aria-label="Street map showing the clinic location"></div>
<div class="hours abs">
  <table>
    <tr><td style="width:63px">Monday:</td><td style="width:57px">8:00-11:00</td><td style="width:74px">2:00-5:00</td><td style="width:50px">Friday:</td><td style="width:57px">8:00-10:00</td><td>1:00-5:00</td></tr>
    <tr><td>Tuesday:</td><td>8:30-11:00</td><td>2:00-5:30</td><td>Saturday:</td><td>CLOSED</td><td></td></tr>
    <tr><td>Wednesday:</td><td>8:00-11:00</td><td>2:00-5:00</td><td>Sunday:</td><td>CLOSED</td><td></td></tr>
    <tr><td>Thursday:</td><td>10:00-12:00</td><td>2:30-5:00</td><td></td><td></td><td></td></tr>
  </table>
</div>
<div class="social abs"><i></i><i></i><i></i></div>
<div class="f-rule abs"></div>
<div class="f-nav abs">Home &nbsp;| &nbsp;Meet Our Staff &nbsp;| &nbsp;Patient Testimonials &nbsp;| &nbsp;Videos &nbsp;| &nbsp;Work Place Wellness &nbsp;| &nbsp;Contact</div>
<div class="copy abs">© 2014 Company Name &nbsp;All right reserved &nbsp;Term of Use</div>
<div class="powered abs">Powered by Tandem Pixel Works</div>

</body>
</html>
```